Website Home Page for Women's Health Medical Office

Redesign existing homepage for website using existing logo. Current website location is www.lumawomenscare.com. Please give it a modern, streamlined, playful feel.

Please give it a feminine feel and make it bright and cheerful using logo colors.

Target Market(s)

Women between the ages of 25-45

Industry/Entity Type

Medical Office

Coding

Coded - Design and coding required

Number of Pages Required

1 page

Font styles to use
Sans Serif
Other font styles liked:
• SEGOI UI script for text and GIL SANS for bold (or their equivilent)

Colors
E54698
E96AAD
F1A4CE
F9D9EA
FCEFF6

Requirements
Must have
• Existing logo. Logo Colors. Feminine, cheerful, simple design. all relevant contact information
Nice to have
• clean lines and streamlined look
Should not have
• Cluttered

```html
<!DOCTYPE html>
<html lang="en">
<head>
<meta charset="utf-8">
<title>Luma Women's Care — Home</title>
<link href="https://fonts.googleapis.com/css2?family=Cabin:wght@400;600;700&family=Noto+Sans:wght@300;400&display=swap" rel="stylesheet">
<style>
:root{
  --pink:#E54698;
  --pink-mid:#E96AAD;
  --pink-soft:#F1A4CE;
  --pink-pale:#F9D9EA;
  --pink-wash:#FCEFF6;
  --ink:#2b2b2b;
  --grey:#555;
  --white:#fff;
}
*{margin:0;padding:0;box-sizing:border-box}
html,body{width:1200px;height:3263px;overflow:hidden}
body{position:relative;font-family:"Noto Sans",sans-serif;font-weight:300;color:var(--ink);background:var(--white)}
.abs{position:absolute}
.backdrop{position:absolute;left:0;top:0}

/* top bar */
.topbar{left:0;top:0;width:1200px;height:33px;background:var(--pink);color:var(--white);font-size:10px;line-height:11px}
.topbar .item{position:absolute;top:5px;display:flex;align-items:center;gap:6px;white-space:nowrap}
.topbar .item.single{top:10px}
.topbar svg{flex:none}

/* header */
.brand{left:108px;top:52px;display:flex;align-items:center;gap:10px}
.brand-mark{width:34px;height:34px;border-radius:50%;background:var(--pink-soft)}
.brand-name{font-family:"Cabin",sans-serif;font-weight:600;font-size:18px;color:var(--ink)}
.nav{top:59px;left:0;font-size:13.5px;color:var(--ink)}
.nav a{position:absolute;white-space:nowrap;color:inherit;text-decoration:none}
.nav a.active{color:var(--pink)}
.nav a.active::after{content:"";position:absolute;left:-4px;right:-4px;bottom:-9px;height:2px;background:var(--pink)}
.caret{display:inline-block;width:6px;height:6px;border-right:1px solid var(--ink);border-bottom:1px solid var(--ink);transform:rotate(45deg);margin-left:4px;position:relative;top:-3px}

/* hero */
.hero-photo{left:0;top:33px;width:1200px;height:646px;
  background:linear-gradient(90deg,#f7f7f7 0%,#f1f0f0 45%,#d9d6d8 62%,#8f8e95 78%,#c9c6c8 92%,#efeeee 100%)}
.eyebrow{font-family:"Cabin",sans-serif;font-weight:700;letter-spacing:.5px;text-transform:uppercase;white-space:nowrap}
.display{font-family:"Cabin",sans-serif;font-weight:400;color:var(--pink);line-height:1}
.hero .eyebrow{left:108px;top:238px;font-size:21px;color:var(--grey)}
.hero .display{left:105px;top:266px;font-size:64px;line-height:62px}
.hero p{left:108px;top:406px;width:440px;font-size:15.5px;line-height:20px;color:var(--ink)}
.btn{display:flex;align-items:center;justify-content:center;border-radius:30px;font-family:"Cabin",sans-serif;font-weight:700;font-size:14px;letter-spacing:.6px;text-transform:uppercase}
.btn-outline{border:3px solid var(--pink);color:var(--pink)}
.hero .btn{left:106px;top:493px;width:247px;height:50px}

/* services */
.services .eyebrow{left:0;width:1225px;text-align:center;top:780px;font-size:20px;color:var(--grey)}
.services .display{left:0;width:1215px;text-align:center;top:806px;font-size:54px}
.service{width:256px;text-align:center}
.service .photo{width:256px;height:256px;border-radius:50%;margin:0 auto}
.service h3{margin-top:28px;font-family:"Cabin",sans-serif;font-weight:700;font-size:22px;color:var(--pink);text-transform:uppercase;letter-spacing:.3px;white-space:nowrap}
.service p{margin:4px auto 0;width:250px;font-size:12.5px;line-height:16px;color:var(--ink)}
.service.featured .photo{box-shadow:0 0 0 5px var(--pink-wash),0 0 0 8px var(--pink)}

/* serving */
.serving .eyebrow{left:111px;top:1656px;font-size:20px;color:var(--white)}
.serving .display{left:104px;top:1682px;font-size:58px;line-height:52px;color:var(--white)}
.serving .copy{left:106px;top:1862px;width:420px;font-size:13px;line-height:16px;color:var(--white)}
.serving .copy p+p{margin-top:16px}
.serving .btn-light{border:3px solid var(--white);color:var(--white)}
.serving .btn-solid{background:var(--white);color:var(--pink)}
.arch-photo{left:649px;top:1508px;width:447px;height:684px;border-radius:224px 224px 200px 200px;
  background:linear-gradient(160deg,#d9d8d6 0%,#eae8e5 35%,#b9b5ad 60%,#6f6b5e 85%,#8a8578 100%)}

/* specialists */
.specialists .eyebrow{left:106px;top:2472px;font-size:20px;color:#444}
.specialists .display{left:103px;top:2500px;font-size:56px;line-height:54px}
.specialists .copy{left:106px;top:2630px;width:440px;font-size:12.5px;line-height:16px;color:#333}
.specialists .copy p+p{margin-top:16px}

/* footer */
.social{top:3086px;left:551px;display:flex;gap:8px}
.social span{width:24px;height:24px;border-radius:4px;background:var(--white);opacity:.9}
.footer-nav{left:0;width:1200px;text-align:center;color:var(--white);font-size:14px}
.footer-nav a{color:inherit;text-decoration:none;margin:0 18px}
.copyright{left:0;width:1200px;text-align:center;top:3210px;color:var(--white);font-size:13px}
</style>
</head>
<body>

<svg class="backdrop" width="1200" height="3263" viewBox="0 0 1200 3263">
  <defs>
    <linearGradient id="careGrad" x1="0" y1="0" x2="1" y2="0">
      <stop offset="0" stop-color="#f2f0f2"/>
      <stop offset=".35" stop-color="#e6e3e6"/>
      <stop offset=".55" stop-color="#c9c4c6"/>
      <stop offset=".72" stop-color="#8a93a5"/>
      <stop offset="1" stop-color="#6c7890"/>
    </linearGradient>
  </defs>
  <rect x="0" y="679" width="1200" height="800" fill="var(--pink-wash)"/>
  <g role="img" aria-label="Photo: a provider gently holding a patient's hands">
    <rect x="0" y="2220" width="1200" height="860" fill="url(#careGrad)"/>
  </g>
  <path fill="var(--pink)" d="M0,1482 C120,1540 230,1562 340,1556 C520,1546 680,1436 880,1436 C1000,1436 1100,1448 1200,1456 L1200,2310 C1100,2286 1010,2254 930,2256 C760,2262 600,2272 420,2300 C260,2322 120,2320 0,2300 Z"/>
  <path fill="var(--pink)" d="M0,3040 C150,3018 260,3004 380,3018 C560,3040 700,3032 860,3022 C1000,3014 1100,3022 1200,3032 L1200,3263 L0,3263 Z"/>
</svg>

<div class="abs topbar">
  <div class="item" style="left:108px">
    <svg width="12" height="12" viewBox="0 0 24 24"><path fill="#fff" d="M6.6 10.8a15.1 15.1 0 0 0 6.6 6.6l2.2-2.2a1 1 0 0 1 1-.25 11.4 11.4 0 0 0 3.6.57 1 1 0 0 1 1 1V20a1 1 0 0 1-1 1A17 17 0 0 1 3 4a1 1 0 0 1 1-1h3.5a1 1 0 0 1 1 1c0 1.25.2 2.45.57 3.57a1 1 0 0 1-.25 1z"/></svg>
    <span>(555) 014 2270<br>(555) 014 2281</span>
  </div>
  <div class="item single" style="left:212px">
    <svg width="15" height="11" viewBox="0 0 15 11"><rect x=".5" y=".5" width="14" height="10" fill="none" stroke="#fff"/><path d="M.5.5 7.5 6l7-5.5" fill="none" stroke="#fff"/></svg>
    <span>hello@lumawomenscare.com</span>
  </div>
  <div class="item" style="left:384px;top:8px">
    <svg width="11" height="15" viewBox="0 0 11 15"><path fill="#fff" d="M5.5 0A5.5 5.5 0 0 0 0 5.5C0 9.6 5.5 15 5.5 15S11 9.6 11 5.5A5.5 5.5 0 0 0 5.5 0zm0 7.6a2.1 2.1 0 1 1 0-4.2 2.1 2.1 0 0 1 0 4.2z"/></svg>
    <span>4180 Linden Avenue, Suite 210, Brookvale, CA 90000</span>
  </div>
</div>

<section class="hero">
  <div class="abs hero-photo" role="img" aria-label="Photo: expectant mother holding a mug in a bright kitchen"></div>
  <div class="abs brand"><span class="brand-mark"></span><span class="brand-name">Luma Women's Care</span></div>
  <nav class="abs nav">
    <a class="active" style="left:414px">Home</a>
    <a style="left:489px">Services<span class="caret"></span></a>
    <a style="left:573px">Resources<span class="caret"></span></a>
    <a style="left:671px">About Us</a>
    <a style="left:762px">Contact Us</a>
  </nav>
  <div class="abs eyebrow">Welcome to Luma Women's Care</div>
  <h1 class="abs display">Better Health<br>Starts Now</h1>
  <p class="abs">We take time to listen to our patients concerns, explain each option available, and to answer any questions our patients may have so that they can make informed decisions.</p>
  <a class="abs btn btn-outline">Make Appointment</a>
</section>

<section class="services">
  <div class="abs eyebrow">How can we help you</div>
  <h2 class="abs display">Our Services</h2>
  <div class="abs service" style="left:53px;top:924px">
    <div class="photo" role="img" aria-label="Photo: pregnancy ultrasound appointment" style="background:linear-gradient(135deg,#5b8aa6,#c9b8a6 55%,#e8e2dc)"></div>
    <h3>Pregnancy Care</h3>
    <p>Receiving regular care in pregnancy is important for the health of both you and your baby. Our obstetricians work with you every step of the way during your pregnancy and delivery to make sure your individual needs are met and co ensure this special journey is a memorable one.</p>
  </div>
  <div class="abs service" style="left:339px;top:924px">
    <div class="photo" role="img" aria-label="Photo: woman taking a pill with a glass of water" style="background:linear-gradient(135deg,#dfe9ee,#c7a58f 50%,#f3eeee)"></div>
    <h3>Birth Control</h3>
    <p>Our gynecologists are knowledgeable on all forms of birth control including the IUD, the implant, vaginal ring insertion, birth control pills, and more! We would love to work with you to determine the best option for you and your lifestyle.</p>
  </div>
  <div class="abs service featured" style="left:622px;top:924px">
    <div class="photo" role="img" aria-label="Photo: provider showing a patient ultrasound images" style="background:linear-gradient(135deg,#b78fa6,#e3b6cf 50%,#9f7990)"></div>
    <h3>Well Woman Exams</h3>
    <p>Our providers will help you to stay healthy by performing a physical exam on you annually. We will screen you for multiple health conditions that may pose a risk to you. This includes screening you for cancerous conditions of the breast, ovaries and cervix.</p>
  </div>
  <div class="abs service" style="left:901px;top:924px">
    <div class="photo" role="img" aria-label="Photo: doctor working at a laptop in a clinic" style="background:linear-gradient(135deg,#e9eef2,#3c6f9a 55%,#d6dde4)"></div>
    <h3>Women's Health</h3>
    <p>Whether you are dealing with painful or irregular periods, fibroids, or other women's health issues, we can help. We offer a variety of the most up-to-date treatment options to help you regain your lifestyle.</p>
  </div>
</section>

<section class="serving">
  <div class="abs arch-photo" role="img" aria-label="Photo: doctor reviewing a clipboard with a smiling patient"></div>
  <div class="abs eyebrow">Personalized health care you deserve</div>
  <h2 class="abs display">Serving Willow<br>Springs Medical<br>Center</h2>
  <div class="abs copy">
    <p>At Luma Women's Care in Brookvale, California, we believe better health starts when the patient is educated. At Luma Women's Care, our providers tailor every procedure performed and treatment option recommended to meet the specific needs of our patients. We remain up-to-date on the latest technology and practice guidelines for women's health.</p>
    <p>Our medical providers will take time to give you the personalized health care you deserve. This includes taking time to listen to you and screening you for problems to help ensure that any health issues are diagnosed and treated as early as possible.</p>
  </div>
  <a class="abs btn btn-light" style="left:106px;top:2055px;width:231px;height:51px">Make Appointment</a>
  <a class="abs btn btn-solid" style="left:355px;top:2055px;width:177px;height:51px">Call Us</a>
</section>

<section class="specialists">
  <div class="abs eyebrow">Exclusively female providers</div>
  <h2 class="abs display">Your OB/GYN<br>Specialists</h2>
  <div class="abs copy">
    <p>Luma Women's Care offers you the best care possible in a personalized setting. We are currently accepting patients. Call our office now to make an appointment.</p>
    <p>Luma Women's Care (located near Willow Springs Hospital in Brookvale, CA) is a medical office that specializes in Christ-centered healthcare for women of all ages. Our team of exclusively female providers have years of experience taking care of women with a variety of pregnancy and gynecology concerns.</p>
    <p>Whether you need a routine examination, help during your pregnancy, have questions on birth control, or another female concern, we offer the best care possible for our patients. That is why better health starts here.</p>
    <p>Our office provides you with an environment where you can feel comfortable and where you know you will be in good hands. Our providers are leaders women's health. Dr. Marlow is a board certified obstetrician and gynecologist. Dr. Ferrante is a board eligible obstetrician and gynecologist.</p>
  </div>
</section>

<footer>
  <div class="abs social"><span></span><span></span><span></span></div>
  <nav class="abs footer-nav" style="top:3138px">
    <a>Home</a><a>Services</a><a>Resources</a><a>About Us</a><a>Contact Us</a>
  </nav>
  <nav class="abs footer-nav" style="top:3159px">
    <a>Privacy Policy</a><a>News</a>
  </nav>
  <div class="abs copyright">Copyright 2022 Reserved</div>
</footer>

</body>
</html>
```